Branded Powerpoint Slide update

Design a clean, modern, professional corporate powerpoint template that include the BrightWell Corporation word-mark logo, brand color, and brand font. The design should come with a variety of sample pages - I have attached a Template sample of what the template should include. I have also included a sample slide that contains newly created brand elements. Feel free to use this as a guide.
Templates should be produced in A4 and Letter formats as a powerpoint file and should use Helvetica Now Display as the embedded font.
Design Preferences:
Cover should stand alone with engaging elements. Overall, design elements should remain minimal as to not dominate the slide. Colour block designs, solid borders with flowing smooth lines, single side borders with connected header and footer, cut off or half page headers and footers are all acceptable.
Enclosed are:
1. Three word mark logos with reverse versions of each, one for each primary brand colour. ('b-invert, o-invert, 0-main, b-main)
2. BrightWell corporate colour pallet (brightwell brand... )
3. Helvetica Now Display font files
4. Sample of Powerpoint template to show types of pages needed for inclusion ('Sample Slide Deck.ppt)
5. Sample of newly created brand elements for simple Header/Text Body slide. (both 'letterhead...ai" files are the raw files. 'Powerpoint slide Template Sample' is the sample being used).

```html
<!DOCTYPE html>
<html lang="en">
<head>
<meta charset="utf-8">
<title>BrightWell Slide Template</title>
<link href="https://fonts.googleapis.com/css2?family=Montserrat:wght@800&family=IBM+Plex+Sans:wght@400;500&display=swap" rel="stylesheet">
<style>
  :root{
    --page:#d6d6d8;
    --slide:#ffffff;
    --ink:#131a2a;
    --navy:#131a2a;
    --blue:#1ea0f5;
    --red:#ff3a12;
    --rule:#e5321e;
    --purple:#5b1a8e;
    --orange:#f5581f;
    --grid:#e6e6ea;
    --muted:#a8a8b0;
  }
  *{box-sizing:border-box;margin:0;padding:0}
  html,body{width:1200px;height:4265px;overflow:hidden;background:var(--page)}
  body{position:relative;font-family:"IBM Plex Sans",Arial,sans-serif;color:var(--ink)}
  .slide{position:absolute;left:88px;width:1018px;height:763px;background:var(--slide);overflow:hidden}
  .slide-header{position:absolute;left:0;top:0;width:1018px;height:46px;display:block}
  .slide-footer{position:absolute;left:0;top:737px;width:1018px;height:26px}
  .footer-rule-left{position:absolute;left:0;top:0;width:18px;height:8px;background:var(--rule)}
  .footer-rule{position:absolute;left:168px;top:0;right:0;height:8px;background:var(--rule)}
  .footer-wordmark{position:absolute;left:22px;top:-22px;font-family:"Montserrat",sans-serif;font-weight:800;font-size:27px;color:var(--blue);letter-spacing:-0.5px;line-height:1}
  .footer-domain{position:absolute;right:2px;top:-1px;font-size:8px;color:#fff;line-height:10px}
  .heading{font-family:"Montserrat",sans-serif;font-weight:800;text-transform:uppercase;letter-spacing:-0.3px;color:var(--ink)}

  /* Slide 1 */
  .s1-title{position:absolute;left:70px;top:166px;font-size:29px}
  .bullets{position:absolute;left:70px;top:262px;list-style:none}
  .bullets li{position:relative;padding-left:26px;font-size:22px;line-height:32px;margin-bottom:31px;text-transform:uppercase}
  .bullets li::before{content:"";position:absolute;left:2px;top:10px;border-left:8px solid var(--blue);border-top:6px solid transparent;border-bottom:6px solid transparent}
  .s1-body{position:absolute;left:70px;top:494px;width:900px;font-size:22px;line-height:34px}

  /* Slide 2 */
  .s2-title{position:absolute;left:73px;top:112px;font-size:30px}
  .member{position:absolute;top:227px;width:240px;text-align:center}
  .portrait{width:212px;height:212px;border-radius:50%;margin:0 auto}
  .member-name{margin-top:28px;font-family:"Montserrat",sans-serif;font-weight:800;font-size:18px}
  .member-role{font-size:19px;line-height:26px}
  .member-bio{margin-top:12px;font-size:16px;line-height:21px}

  /* Slide 3 */
  .column{position:absolute;top:200px;width:280px}
  .column h2{font-size:30px;margin-bottom:12px}
  .column p{font-size:19px;line-height:27.6px}

  /* Slide 4 */
  .s4-title{position:absolute;left:0;right:0;top:140px;text-align:center;font-size:30px;line-height:51px}
  .chart{position:absolute;left:0;top:0}
  .chart text{font-family:"IBM Plex Sans",sans-serif;font-size:12px;fill:var(--muted)}

  /* Slide 5 */
  .welcome{position:absolute;left:86px;top:188px}
  .welcome-kicker{font-size:31px}
  .welcome-name{font-family:"Montserrat",sans-serif;font-weight:800;font-size:62px;letter-spacing:-1px;line-height:72px;margin-top:4px}
  .welcome-body{margin-top:20px;width:510px;font-size:24px;line-height:34px}
  .hero-photo{position:absolute;left:708px;top:46px;width:310px;height:691px;background:radial-gradient(circle at 55% 45%,#7fb4dc 0%,#2c4a6a 22%,#141d2c 60%,#0b0f18 100%)}
</style>
</head>
<body>

<svg width="0" height="0" style="position:absolute">
  <defs>
    <g id="brand-header">
      <polygon points="0,0 712,0 702,46 0,46" fill="#131a2a"/>
      <polygon points="718,0 930,0 920,46 708,46" fill="#1ea0f5"/>
      <polygon points="936,0 1018,0 1018,46 926,46" fill="#ff3a12"/>
    </g>
  </defs>
</svg>

<!-- Slide 1: Title and bullets -->
<section class="slide" style="top:141px">
  <svg class="slide-header" viewBox="0 0 1018 46"><use href="#brand-header"/></svg>
  <h1 class="heading s1-title">Lorem ipsum dolor sit amet consectetur</h1>
  <ul class="bullets">
    <li>Lorem ipsum dolor sit amet consectetur</li>
    <li>Sed ut perspiciatis unde omnis iste</li>
    <li>Ut enim ad minima veniam, quis nostrum exercitationem</li>
  </ul>
  <p class="s1-body">On the other hand, we denounce with righteous indignation and dislike men who are so beguiled and demoralized by the charms of pleasure of the moment.</p>
  <footer class="slide-footer"><span class="footer-rule-left"></span><span class="footer-wordmark">BrightWell</span><span class="footer-rule"></span><span class="footer-domain">brightwell.com</span></footer>
</section>

<!-- Slide 2: Team -->
<section class="slide" style="top:968px">
  <svg class="slide-header" viewBox="0 0 1018 46"><use href="#brand-header"/></svg>
  <h1 class="heading s2-title">Team</h1>
  <div class="member" style="left:24px">
    <div class="portrait" role="img" aria-label="Portrait photo of team member" style="background:linear-gradient(135deg,#c9c4bd,#6b5a4c 55%,#c65a48)"></div>
    <div class="member-name">RICHARD</div><div class="member-role">Manager</div>
    <p class="member-bio">Lorem ipsum dolor sit amet consectetur adip iscing elit sed.</p>
  </div>
  <div class="member" style="left:269px">
    <div class="portrait" role="img" aria-label="Portrait photo of team member" style="background:linear-gradient(135deg,#22333f,#8a6a58 55%,#1c2a33)"></div>
    <div class="member-name">RICHARD</div><div class="member-role">Manager</div>
    <p class="member-bio">Lorem ipsum dolor sit amet consectetur adip iscing elit sed.</p>
  </div>
  <div class="member" style="left:517px">
    <div class="portrait" role="img" aria-label="Portrait photo of team member" style="background:linear-gradient(135deg,#9aa6b8,#4a5060 50%,#1a1d24)"></div>
    <div class="member-name">RICHARD</div><div class="member-role">Manager</div>
    <p class="member-bio">Lorem ipsum dolor sit amet consectetur adip iscing elit sed.</p>
  </div>
  <div class="member" style="left:755px">
    <div class="portrait" role="img" aria-label="Portrait photo of team member" style="background:linear-gradient(135deg,#7f8a6a,#a7a9b4 55%,#5a6048)"></div>
    <div class="member-name">RICHARD</div><div class="member-role">Manager</div>
    <p class="member-bio">Lorem ipsum dolor sit amet consectetur adip iscing elit sed.</p>
  </div>
  <footer class="slide-footer"><span class="footer-rule-left"></span><span class="footer-wordmark">BrightWell</span><span class="footer-rule"></span><span class="footer-domain">brightwell.com</span></footer>
</section>

<!-- Slide 3: Three columns -->
<section class="slide" style="top:1781px">
  <svg class="slide-header" viewBox="0 0 1018 46"><use href="#brand-header"/></svg>
  <div class="column" style="left:50px">
    <h2 class="heading">Lorem ipsum</h2>
    <p>At vero eos et accusamus et iusto odio dignissimos duci mus qui blanditiis praesentium voluptatum deleniti atque corrupti quos dolores et quas molestias excepturi sint occa ecati cupiditate non provident, similique sunt in culpa qui offic ia deserunt mollitia animi, id est laborum</p>
  </div>
  <div class="column" style="left:374px">
    <h2 class="heading">Lorem ipsum</h2>
    <p>At vero eos et accusamus et iusto odio dignissimos duci mus qui blanditiis praesentium voluptatum deleniti atque corrupti quos dolores et quas molestias excepturi sint occa ecati cupiditate non provident, similique sunt in culpa qui offic ia deserunt mollitia animi, id est laborum</p>
  </div>
  <div class="column" style="left:713px">
    <h2 class="heading">Lorem ipsum</h2>
    <p>At vero eos et accusamus et iusto odio dignissimos duci mus qui blanditiis praesentium voluptatum deleniti atque corrupti quos dolores et quas molestias excepturi sint occa ecati cupiditate non provident, similique sunt in culpa qui offic ia deserunt mollitia animi, id est laborum</p>
  </div>
  <footer class="slide-footer"><span class="footer-rule-left"></span><span class="footer-wordmark">BrightWell</span><span class="footer-rule"></span><span class="footer-domain">brightwell.com</span></footer>
</section>

<!-- Slide 4: Chart -->
<section class="slide" style="top:2587px">
  <svg class="slide-header" viewBox="0 0 1018 46"><use href="#brand-header"/></svg>
  <h1 class="heading s4-title">At vero eos et accusamus et iusto<br>odio dignissimos ducimus</h1>
  <svg class="chart" width="1018" height="620" viewBox="0 0 1018 620">
    <g stroke="#e6e6ea" stroke-width="1">
      <line x1="58" y1="364" x2="996" y2="364"/><line x1="58" y1="395" x2="996" y2="395"/>
      <line x1="58" y1="426" x2="996" y2="426"/><line x1="58" y1="457" x2="996" y2="457"/>
      <line x1="58" y1="489" x2="996" y2="489"/><line x1="58" y1="520" x2="996" y2="520"/>
      <line x1="58" y1="551" x2="996" y2="551"/>
      <line x1="58" y1="364" x2="58" y2="551"/><line x1="996" y1="364" x2="996" y2="551"/>
    </g>
    <g text-anchor="end">
      <text x="52" y="368">60</text><text x="52" y="399">50</text><text x="52" y="430">40</text>
      <text x="52" y="461">30</text><text x="52" y="493">20</text><text x="52" y="524">10</text><text x="52" y="555">0</text>
    </g>
    <g fill="#5b1a8e">
      <rect x="88" y="457" width="22" height="94"/><rect x="163" y="504" width="22" height="47"/>
      <rect x="239" y="404" width="22" height="147"/><rect x="314" y="529" width="22" height="22"/>
      <rect x="390" y="442" width="22" height="109"/><rect x="465" y="414" width="22" height="137"/>
      <rect x="541" y="529" width="22" height="22"/><rect x="616" y="392" width="22" height="159"/>
      <rect x="691" y="517" width="22" height="34"/><rect x="767" y="376" width="22" height="175"/>
      <rect x="842" y="457" width="22" height="94"/><rect x="918" y="417" width="22" height="134"/>
    </g>
    <g fill="#f5581f">
      <rect x="121" y="392" width="22" height="159"/><rect x="196" y="373" width="22" height="178"/>
      <rect x="272" y="442" width="22" height="109"/><rect x="347" y="432" width="22" height="119"/>
      <rect x="423" y="492" width="22" height="59"/><rect x="498" y="370" width="22" height="181"/>
      <rect x="574" y="420" width="22" height="131"/><rect x="649" y="454" width="22" height="97"/>
      <rect x="724" y="376" width="22" height="175"/><rect x="800" y="436" width="22" height="115"/>
      <rect x="875" y="392" width="22" height="159"/><rect x="951" y="504" width="22" height="47"/>
    </g>
    <g text-anchor="middle">
      <text x="116" y="575">JAN</text><text x="191" y="575">FEB</text><text x="267" y="575">MAR</text>
      <text x="342" y="575">APR</text><text x="417" y="575">MAY</text><text x="493" y="575">JUN</text>
      <text x="568" y="575">JUL</text><text x="644" y="575">AUG</text><text x="719" y="575">SEP</text>
      <text x="794" y="575">OCT</text><text x="870" y="575">NOV</text><text x="945" y="575">DEC</text>
    </g>
  </svg>
  <footer class="slide-footer"><span class="footer-rule-left"></span><span class="footer-wordmark">BrightWell</span><span class="footer-rule"></span><span class="footer-domain">brightwell.com</span></footer>
</section>

<!-- Slide 5: Welcome -->
<section class="slide" style="top:3406px">
  <svg class="slide-header" viewBox="0 0 1018 46"><use href="#brand-header"/></svg>
  <div class="welcome">
    <div class="heading welcome-kicker">Welcome to</div>
    <div class="welcome-name">BrightWell</div>
    <p class="welcome-body">Lorem ipsum dolor sit amet, consectetur adipiscing elit, sed do eiusmod tempor incididunt ut labore et dolore magna aliqua. Ut enim ad minim veniam, quis nostrud exercitation ullamco laboris nisi ut aliquip ex ea commodo consequat. Duis aute irure dolor in reprehenderit in voluptate velit esse cillum dolore eu fugiat nulla pariatur.</p>
  </div>
  <div class="hero-photo" role="img" aria-label="Photo of a hand touching a glowing digital interface"></div>
  <footer class="slide-footer"><span class="footer-rule-left"></span><span class="footer-wordmark">BrightWell</span><span class="footer-rule"></span><span class="footer-domain">brightwell.com</span></footer>
</section>

</body>
</html>
```